Rocket business card

Modern business card design, use of color is good with clean space too.

Things to include on card:

Quote: I add fuel to your optometry practice

- Eyewear Sales
- Admin Duties
- Revenue Collection
- Leadership
- Tech Adoption
- COGS Reduction
- Product Sourcing
-Medical Growth

Dalton Vessey, CEO
Glint Harbor
Text Me! 847-302-1964
dalton@glintharbor.example

```html
<!DOCTYPE html>
<html lang="en">
<head>
<meta charset="utf-8">
<title>Glint Harbor — Business Card</title>
<link rel="stylesheet" href="https://fonts.googleapis.com/css2?family=Questrial&family=Oswald:wght@500&display=swap">
<style>
  :root {
    --page-bg: #f4f4f4;
    --card-white: #ffffff;
    --navy: #022157;
    --ink: #111111;
    --title-blue: #1a46a0;
    --accent-orange: #f0622a;
    --on-navy: #ffffff;
  }
  html, body {
    margin: 0;
    padding: 0;
    width: 1200px;
    height: 1200px;
    overflow: hidden;
    background: var(--page-bg);
  }
  .business-card {
    position: absolute;
    left: 40px;
    top: 280px;
    width: 1050px;
    height: 600px;
    transform: scale(1.0667);
    transform-origin: top left;
    display: flex;
    box-shadow: 0 6px 24px rgba(0,0,0,0.12);
    font-family: "Questrial", sans-serif;
  }
  .card-front {
    position: relative;
    width: 525px;
    height: 600px;
    background: var(--card-white);
  }
  .card-services {
    position: relative;
    width: 525px;
    height: 600px;
    background: var(--navy);
    color: var(--on-navy);
  }
  .brand {
    position: absolute;
    left: 0;
    top: 72px;
    width: 525px;
    display: flex;
    flex-direction: column;
    align-items: center;
  }
  .brand-dot {
    width: 96px;
    height: 96px;
    border-radius: 50%;
    background: var(--accent-orange);
  }
  .brand-name {
    margin-top: 18px;
    font-size: 50px;
    line-height: 1;
    color: var(--ink);
    letter-spacing: 1px;
  }
  .person {
    position: absolute;
    right: 47px;
    top: 302px;
    text-align: right;
    line-height: 1;
  }
  .person-name {
    font-size: 40px;
    color: var(--ink);
  }
  .person-title {
    margin-top: 10px;
    font-size: 40px;
    color: var(--title-blue);
  }
  .contact {
    position: absolute;
    left: 44px;
    top: 454px;
    list-style: none;
    margin: 0;
    padding: 0;
    font-size: 30px;
    color: var(--ink);
  }
  .contact li {
    display: flex;
    align-items: center;
    height: 41px;
  }
  .contact svg {
    width: 36px;
    height: 30px;
    margin-right: 12px;
    fill: var(--title-blue);
  }
  .service-list {
    position: absolute;
    left: 86px;
    top: 114px;
    margin: 0;
    padding: 0;
    list-style: none;
    font-size: 35px;
    line-height: 45px;
  }
  .service-list li {
    position: relative;
    padding-left: 23px;
  }
  .service-list li::before {
    content: "";
    position: absolute;
    left: 0;
    top: 12px;
    width: 4px;
    height: 4px;
    border-radius: 50%;
    background: var(--on-navy);
  }
  .tagline {
    position: absolute;
    left: 26px;
    top: 520px;
    margin: 0;
    font-family: "Oswald", sans-serif;
    font-weight: 500;
    font-size: 28px;
    letter-spacing: 0.2px;
    text-transform: uppercase;
    transform: scaleX(0.86);
    transform-origin: left center;
    white-space: nowrap;
  }
</style>
</head>
<body>
  <main class="business-card">
    <section class="card-front">
      <div class="brand">
        <div class="brand-dot"></div>
        <div class="brand-name">Glint Harbor</div>
      </div>
      <div class="person">
        <div class="person-name">Dalton Vessey</div>
        <div class="person-title">CEO</div>
      </div>
      <ul class="contact">
        <li>
          <svg viewBox="0 0 36 30" aria-hidden="true">
            <path d="M9 2h25v16H18l-5 4v-4H9z"/>
            <path d="M2 8h5v12h4v4l5-4h10v3H17l-8 6v-6H2z"/>
            <rect x="13" y="6" width="17" height="2.4" fill="#fff"/>
            <rect x="13" y="11" width="13" height="2.4" fill="#fff"/>
          </svg>
          847-302-1964
        </li>
        <li>
          <svg viewBox="0 0 36 30" aria-hidden="true">
            <path d="M2 5h32v20H2z"/>
            <path d="M3 6l15 12L33 6" fill="none" stroke="#fff" stroke-width="2.4"/>
            <path d="M3 24l11-9M33 24l-11-9" fill="none" stroke="#fff" stroke-width="2"/>
          </svg>
          dalton@glintharbor.example
        </li>
      </ul>
    </section>
    <section class="card-services">
      <ul class="service-list">
        <li>Eyewear Sales</li>
        <li>Admin Duties</li>
        <li>Revenue Collection</li>
        <li>Leadership</li>
        <li>Tech Adoption</li>
        <li>COGS Reduction</li>
        <li>Product Sourcing</li>
        <li>Medical Growth</li>
      </ul>
      <p class="tagline">I add fuel to your optometry practice.</p>
    </section>
  </main>
</body>
</html>
```